Rollup Banner & Flyer für eine Messe "Erfolg durch Innovation"

Wir benötigten für eine Messe einen Roll Up Banner und Flyer zum verteilen. Gerne basierend auf der aktuellen Firmenpräsentation und mit unseren Referenzen.
Im flyer sollen unserer Leistungen (Datenanalyse, Simulation, Optimierung und Webapplikation) dargestellt werden mit einem kleinen Text und einem aussagekräftigen bild. (https://www.velkador.ch/leistungen/)

Target Market(s)

Industrie

Industry/Entity Type

Simulation

Font styles to use
Sans Serif
Other font styles liked:
• Roboto

Requirements
Must have
• Logo, Referenzen

```html
<!DOCTYPE html>
<html lang="de">
<head>
<meta charset="utf-8">
<title>Velkador – Flyer & Rollup</title>
<link href="https://fonts.googleapis.com/css2?family=Poppins:wght@400;500;600;700&family=Roboto+Slab:wght@600;700&display=swap" rel="stylesheet">
<style>
:root{
  --lime:#dcdc6a;
  --ink:#0d0d12;
  --black:#000;
  --white:#fff;
  --stage:#a9a9a9;
  --grey:#555;
}
*{box-sizing:border-box;margin:0;padding:0}
html,body{width:1153px;height:1200px;overflow:hidden;background:var(--stage);font-family:"Poppins",sans-serif;color:var(--ink)}
.slab{font-family:"Roboto Slab",serif}
.flyer{position:absolute;left:86px;top:123px;width:486px;height:629px;background:var(--white);overflow:hidden}
.flyer__strip{position:absolute;right:0;top:0;width:88px;height:100%;background:var(--black)}
.brand{position:absolute;display:flex;align-items:center;gap:8px}
.brand__dot{border-radius:50%;background:var(--lime);flex:none}
.brand__name{font-family:"Poppins",sans-serif;font-weight:700;color:var(--lime)}
.flyer .brand{left:35px;top:40px}
.flyer .brand__dot{width:30px;height:30px}
.flyer .brand__name{font-size:28px;line-height:1}
.flyer__title{position:absolute;left:31px;top:88px;font-size:18px;line-height:20px;font-weight:700}
.flyer__title span{color:var(--lime)}
.flyer__intro{position:absolute;left:31px;top:130px;width:215px;font-size:6.6px;line-height:8.3px}
.hero{position:absolute}
.flyer .hero{left:265px;top:13px;width:188px;height:188px}
.photo{border-radius:50%;background:radial-gradient(circle at 40% 45%,#8fa0ad,#4d5a63 55%,#2b2724)}
.tabs{position:absolute;left:32px;top:178px;display:flex;height:22px;font-size:13px;font-weight:700}
.tabs__a{background:var(--lime);color:var(--white);padding:3px 12px 0 12px}
.tabs__b{background:var(--ink);color:var(--lime);padding:2px 12px 0 8px;border-radius:0 11px 11px 0}
.service{position:absolute;left:32px;width:420px;height:66px}
.service--tall{height:70px}
.service__frame{position:absolute;left:22px;top:0;width:340px;height:100%;border:1px solid #ccc;border-right:none;border-radius:16px 0 0 16px}
.service__icon{position:absolute;left:3px;top:13px;width:40px;height:40px;border-radius:50%;background:var(--white);border:3px solid var(--lime);box-shadow:4px 3px 0 var(--ink)}
.service__icon svg{width:100%;height:100%}
.service__title{position:absolute;left:53px;top:7px;font-size:9px;color:#b8b84a;font-weight:600}
.service__text{position:absolute;left:53px;top:20px;width:272px;font-size:6.1px;line-height:7.6px}
.service__tags{position:absolute;left:53px;bottom:6px;display:flex;gap:6px;font-size:6.3px;font-weight:700;line-height:8px}
.service__tags span::before{content:"";display:inline-block;width:4px;height:4px;border-radius:50%;background:var(--lime);margin-right:2px}
.monitor{position:absolute;left:332px;top:-6px;width:88px;height:72px}
.monitor__screen{position:absolute;left:0;top:0;width:88px;height:58px;border:3px solid #111;border-bottom-width:8px;border-radius:3px;background:linear-gradient(#f3f5f7,#dfe6e2)}
.monitor__screen::after{content:"";position:absolute;left:-3px;right:-3px;bottom:-8px;height:8px;background:#d9d9d9}
.monitor__stand{position:absolute;left:34px;top:58px;width:22px;height:12px;background:#cfcfcf;clip-path:polygon(20% 0,80% 0,100% 100%,0 100%)}
.contact{position:absolute;left:35px;top:583px;display:flex;gap:9px;font-size:10.5px;align-items:center;white-space:nowrap}
.contact span{display:flex;align-items:center;gap:5px}
.contact svg{width:13px;height:13px}
.rollup{position:absolute;left:673px;top:123px;width:394px;height:955px;background:var(--white);overflow:hidden}
.rollup .brand{left:64px;top:40px}
.rollup .brand__dot{width:40px;height:40px}
.rollup .brand__name{font-size:40px;line-height:1}
.rollup__dark{position:absolute;left:0;top:124px;width:100%;height:726px;background:radial-gradient(ellipse at 30% 60%,#2a2a2a,#050505 70%)}
.rollup__h1{position:absolute;left:0;width:100%;text-align:center;color:var(--white);font-size:26px;top:141px}
.rollup__h2{position:absolute;left:0;width:100%;text-align:center;color:var(--lime);font-size:45px;line-height:46px;top:180px}
.rollup .hero{left:58px;top:294px;width:280px;height:280px}
.rollup__snake{position:absolute;left:0;top:560px}
.pill{position:absolute;height:28px;font-family:"Roboto Slab",serif;font-weight:700;font-size:18px;line-height:28px;border-radius:14px;white-space:nowrap}
.pill--white{background:var(--white);color:var(--ink);padding-left:18px}
.pill--black{background:var(--ink);color:var(--white);text-align:right;padding-right:14px}
.badge{position:absolute;width:72px;height:72px;border-radius:50%;background:var(--white);border:4px solid var(--white);box-shadow:0 0 0 3px var(--ink)}
.badge--plain{box-shadow:none;width:69px;height:69px}
.badge svg{width:100%;height:100%}
.rollup__url{position:absolute;left:0;width:100%;top:870px;text-align:center;font-size:35px;font-weight:500}
.rollup__url b{color:var(--lime);font-weight:700}
</style>
</head>
<body>

<section class="flyer">
  <div class="flyer__strip"></div>
  <div class="brand"><span class="brand__dot"></span><span class="brand__name">Velkador</span></div>

  <svg class="hero" viewBox="0 0 188 188" aria-hidden="true">
    <path d="M94 4 A90 90 0 1 0 184 94 A84 84 0 0 1 94 178 A84 84 0 0 1 94 4Z" fill="#dcdc6a"/>
    <circle cx="100" cy="94" r="82" fill="none" stroke="#000" stroke-width="12"/>
  </svg>
  <div class="hero photo" role="img" aria-label="Foto: Hände an einem Laptop mit Diagrammen auf dem Bildschirm" style="left:281px;top:37px;width:142px;height:142px"></div>

  <h1 class="flyer__title slab">Du hast eine schwierige<br><span>Entscheidung zu treffen?</span></h1>
  <p class="flyer__intro">Was wäre, wenn wir dir zeigen würden, welche Option die Beste ist? Wir unterstützen Unternehmen in Logistik und Produktion die besten Entscheidungen zu treffen und dass innerhalb weniger Wochen.</p>

  <div class="tabs slab"><span class="tabs__a">Unser</span><span class="tabs__b">Leistungen</span></div>

  <div class="service" style="top:214px">
    <div class="service__frame"></div>
    <div class="service__icon"><svg viewBox="0 0 40 40"><g fill="#555"><rect x="11" y="22" width="3" height="7"/><rect x="15" y="19" width="3" height="10"/><rect x="19" y="21" width="3" height="8"/></g><circle cx="22" cy="16" r="5" fill="none" stroke="#555" stroke-width="2"/><path d="M26 20l4 4" stroke="#555" stroke-width="2"/></svg></div>
    <div class="service__title slab">Datenanalyse</div>
    <p class="service__text">Datenanalyse macht Prozesse sichtbar, erkennt Muster und schafft eine objektive Grundlage für Entscheidungen. Wir strukturieren, bereinigen und analysieren Daten so, dass sie einen echten Nutzen erzeugen.</p>
    <div class="service__tags"><span>Transparent</span><span>Verständlich</span><span>Aussagekräftig</span></div>
    <div class="monitor"><div class="monitor__screen" role="img" aria-label="Bildschirm mit Dashboard zur Datenanalyse"></div><div class="monitor__stand"></div></div>
  </div>

  <div class="service" style="top:308px">
    <div class="service__frame"></div>
    <div class="service__icon"><svg viewBox="0 0 40 40"><rect x="10" y="12" width="20" height="14" rx="1" fill="none" stroke="#555" stroke-width="2"/><circle cx="20" cy="19" r="3.5" fill="#555"/><path d="M16 30h8" stroke="#555" stroke-width="2"/></svg></div>
    <div class="service__title slab">Simulation</div>
    <p class="service__text">Simulation bildet reale Prozesse digital ab, damit Abläufe, Kapazitäten und Varianten risikofrei getestet werden können.</p>
    <div class="service__tags"><span>Vergleichbar</span><span>Belastbar</span><span>Risikoarm</span></div>
    <div class="monitor"><div class="monitor__screen" role="img" aria-label="Bildschirm mit Simulationsmodell auf einer Karte"></div><div class="monitor__stand"></div></div>
  </div>

  <div class="service service--tall" style="top:404px">
    <div class="service__frame"></div>
    <div class="service__icon"><svg viewBox="0 0 40 40"><circle cx="20" cy="20" r="8" fill="none" stroke="#555" stroke-width="4" stroke-dasharray="4 2"/><path d="M15 24l5-5 3 3 6-7" fill="none" stroke="#555" stroke-width="2"/></svg></div>
    <div class="service__title slab">Optimierung</div>
    <p class="service__text">Optimierung sucht automatisch nach der besten Lösung – sei es bei Planung, Ressourcen, Routen oder Abläufen. Mit Algorithmen und intelligenten Modellen finden wir Varianten, die Kosten senken, Kapazitäten besser nutzen und Entscheidungen beschleunigen.</p>
    <div class="service__tags"><span>Efficent</span><span>Zielgerichtet</span><span>Robust</span></div>
    <div class="monitor"><div class="monitor__screen" role="img" aria-label="Bildschirm mit Planungs-Gantt-Diagramm"></div><div class="monitor__stand"></div></div>
  </div>

  <div class="service service--tall" style="top:495px">
    <div class="service__frame"></div>
    <div class="service__icon"><svg viewBox="0 0 40 40"><circle cx="20" cy="17" r="4" fill="#555"/><path d="M13 28a7 6 0 0 1 14 0z" fill="#555"/><circle cx="11" cy="13" r="2" fill="#555"/><circle cx="29" cy="13" r="2" fill="#555"/><circle cx="20" cy="9" r="2" fill="#555"/></svg></div>
    <div class="service__title slab">Webapplikationen</div>
    <p class="service__text">Wir entwickeln individuelle Webapplikationen, die Daten, Simulationen und Optimierungen in einem benutzerfreundlichen Tool zusammenführen. So entstehen Lösungen, die direkt im Alltag genutzt werden – einfach, schnell und ohne Installation.</p>
    <div class="service__tags"><span>Zugänglich</span><span>Verfugtbar</span><span>Flexibel</span></div>
    <div class="monitor"><div class="monitor__screen" role="img" aria-label="Bildschirm mit Webapplikation und Balkendiagramm"></div><div class="monitor__stand"></div></div>
  </div>

  <div class="contact">
    <span><svg viewBox="0 0 14 14"><circle cx="7" cy="7" r="7" fill="#0d0d12"/><path d="M4.5 3.5l1.5 0 .6 2-1 .8a5 5 0 0 0 2.1 2.1l.8-1 2 .6v1.5c-4 .5-6.4-2-6-6z" fill="#dcdc6a"/></svg>+41 81 555 40 20</span>
    <span><svg viewBox="0 0 14 14"><circle cx="7" cy="7" r="7" fill="#0d0d12"/><rect x="3.5" y="4.5" width="7" height="5" fill="none" stroke="#dcdc6a"/><path d="M3.5 4.5l3.5 3 3.5-3" fill="none" stroke="#dcdc6a"/></svg>info@velkador.ch</span>
    <span><svg viewBox="0 0 14 14"><circle cx="7" cy="7" r="7" fill="#0d0d12"/><circle cx="7" cy="7" r="3.5" fill="none" stroke="#dcdc6a"/><path d="M3.5 7h7M7 3.5v7" stroke="#dcdc6a" stroke-width=".7"/></svg>www.velkador.ch</span>
  </div>
</section>

<section class="rollup">
  <div class="brand"><span class="brand__dot"></span><span class="brand__name">Velkador</span></div>
  <div class="rollup__dark"></div>
  <h1 class="rollup__h1 slab">Du hast eine schwierige</h1>
  <h2 class="rollup__h2 slab">Entscheidung<br>zu treffen?</h2>

  <svg class="hero" viewBox="0 0 280 280" aria-hidden="true">
    <path d="M140 4 A136 136 0 1 0 276 140 A126 126 0 0 1 140 266 A126 126 0 0 1 140 4Z" fill="#dcdc6a"/>
    <circle cx="145" cy="140" r="128" fill="none" stroke="#fff" stroke-width="10"/>
  </svg>
  <div class="hero photo" role="img" aria-label="Foto: Hand mit Stift an einem Laptop mit Diagrammen" style="left:96px;top:327px;width:208px;height:208px;background:radial-gradient(circle at 45% 40%,#d9e6ea,#9fb3b8 60%,#6f7f82)"></div>

  <svg class="rollup__snake" width="394" height="300" viewBox="0 0 394 300" aria-hidden="true">
    <rect x="112" y="32" width="282" height="27" fill="#dcdc6a"/>
    <path d="M394 73 H165 A28 28 0 0 0 165 129 H255 A29 29 0 0 1 255 187 H165 A29 29 0 0 0 165 245 H60" fill="none" stroke="#dcdc6a" stroke-width="46"/>
    <rect x="0" y="266" width="290" height="26" fill="#dcdc6a"/>
  </svg>

  <div class="pill pill--white" style="left:127px;top:619px;width:267px">Datenanalyse</div>
  <div class="pill pill--black" style="left:120px;top:676px;width:142px">Simulation</div>
  <div class="pill pill--white" style="left:127px;top:735px;width:267px">Optimierung</div>
  <div class="pill pill--black" style="left:66px;top:792px;width:196px">Webapplikationen</div>

  <div class="badge badge--plain" style="left:46px;top:600px"><svg viewBox="0 0 64 64"><g fill="#555"><rect x="16" y="36" width="5" height="12"/><rect x="23" y="32" width="5" height="16"/><rect x="30" y="35" width="5" height="13"/></g><circle cx="36" cy="25" r="8" fill="none" stroke="#555" stroke-width="3"/><path d="M42 31l7 7" stroke="#555" stroke-width="4"/></svg></div>
  <div class="badge" style="left:272px;top:648px"><svg viewBox="0 0 64 64"><rect x="16" y="18" width="32" height="22" rx="2" fill="none" stroke="#555" stroke-width="3"/><circle cx="32" cy="29" r="6" fill="#555"/><path d="M26 46h12" stroke="#555" stroke-width="3"/></svg></div>
  <div class="badge badge--plain" style="left:46px;top:715px"><svg viewBox="0 0 64 64"><circle cx="32" cy="32" r="13" fill="none" stroke="#555" stroke-width="6" stroke-dasharray="6 3"/><path d="M24 38l8-8 4 4 10-11" fill="none" stroke="#555" stroke-width="3"/></svg></div>
  <div class="badge" style="left:272px;top:765px"><svg viewBox="0 0 64 64"><circle cx="32" cy="28" r="6" fill="#555"/><path d="M21 45a11 9 0 0 1 22 0z" fill="#555"/><circle cx="17" cy="22" r="3" fill="#555"/><circle cx="47" cy="22" r="3" fill="#555"/><circle cx="32" cy="13" r="3" fill="#555"/></svg></div>

  <div class="rollup__url">www.<b>velkador</b>.ch</div>
</section>

</body>
</html>
```